Maravel - Refresh the look and feel of an existing website

We currently have an existing website www.maravelpartnersgroup.example however it needs a more refreshed 'look and feel'. We are a professional consultancy that works with large corporate organisations and government. Our 'tag line' is A New Way of Thinking. We want the site to communicate "Innovation" and Leading Edge Thinking.

Target Market(s)

Corporate and Professional Clients - Organisation and Business Change

Industry/Entity Type

Management Consulting

Number of Pages Required

1 page

Font styles to use
Sans Serif

Requirements
Must have
• Must have a professional Corporate look and feel. Header 'imagery' is ok but boxes on front page need changing ... along with the words. The focus on home page needs to 'call out' 3 main consulting areas:-
• - Change & Transformation Specialists
• - Innovative Solutions
• - Digital Transformation
• Tag Line for business is ... A New Way of Thinking (Highlighting Maravel as 'Thought Leaders' in business)
Nice to have
• Less "words' more imagery. Possibly an area for a 'video' or recent articles/blogs on the front page. Needs to have more of an 'interactive' feel. We are open to suggestions.
Should not have
• NA

```html
<!DOCTYPE html>
<html lang="en">
<head>
<meta charset="utf-8">
<title>Maravel Global Solutions</title>
<link href="https://fonts.googleapis.com/css2?family=Open+Sans:wght@400;600;700;800&display=swap" rel="stylesheet">
<style>
:root{
  --navy:#243b5a;
  --navy-dark:#1e3350;
  --nav-band:#cfe2ee;
  --text:#5b6b7d;
  --link:#3d64a4;
  --white:#ffffff;
  --footer-text:#b7c4d4;
  --footer-link:#7f93ad;
}
*{margin:0;padding:0;box-sizing:border-box}
html,body{width:750px;height:1200px;overflow:hidden;background:var(--white)}
body{font-family:"Open Sans",sans-serif;color:var(--text);position:relative}
.abs{position:absolute}

/* header */
.brand{left:44px;top:15px;display:flex;align-items:center;gap:8px}
.brand-dot{width:36px;height:36px;border-radius:50%;background:var(--navy)}
.brand-name{font-size:19px;font-weight:700;color:var(--navy);letter-spacing:.5px}
.phone{left:322px;top:22px;display:flex;align-items:center;gap:18px;font-size:14px;font-style:italic;color:#6f7c8b}
.social{right:66px;top:23px;display:flex;gap:4px}
.social span{width:16px;height:16px;border-radius:50%;background:#333}

/* nav */
.nav{left:0;top:68px;width:750px;height:36px;background:var(--nav-band)}
.nav ul{list-style:none;display:flex;position:absolute;left:46px;top:5px}
.nav li{font-size:10.5px;font-weight:600;color:var(--navy);padding:0 12px;height:24px;line-height:24px;letter-spacing:.3px}
.nav li.active{background:var(--navy);color:var(--white);padding:0 18px;margin-right:6px}
.nav .divider{position:absolute;left:576px;top:8px;width:1px;height:19px;background:#9fb3c4}
.nav .search{position:absolute;right:66px;top:11px;font-size:9px;font-style:italic;color:#8a9aab}

/* hero */
.hero{left:0;top:104px;width:750px;height:279px;overflow:hidden}
.hero-photo{position:absolute;inset:0;background:linear-gradient(90deg,#1aa4d6 0%,#2bb0dd 18%,#8d9aa3 30%,#b7c5cf 52%,#d9e6ee 75%,#cbd2c0 100%)}
.hero-photo::after{content:"";position:absolute;left:0;right:0;bottom:0;height:90px;background:linear-gradient(180deg,rgba(120,125,130,0),rgba(130,130,132,.75))}
.hero-arrow{position:absolute;top:110px}
.tagline{position:absolute;left:235px;top:170px;padding:10px 22px;background:rgba(255,255,255,.82);font-size:34px;font-weight:700;color:var(--navy);letter-spacing:.5px;white-space:nowrap;line-height:1.2}

/* features */
.feature{width:190px;top:427px}
.feature h3{font-size:9.5px;font-weight:700;color:#2d3e50;letter-spacing:.6px;white-space:nowrap}
.feature p{font-size:9px;line-height:15px;letter-spacing:.2px}
.read-more{font-size:9px;font-weight:600;color:var(--link);display:flex;align-items:center;gap:10px}
.section-title{left:0;width:730px;top:614px;text-align:center;font-size:13px;font-weight:700;color:var(--navy);letter-spacing:.8px}

/* blog */
.post{width:197px;top:661px}
.post-photo{width:197px;height:131px}
.post .meta{margin-top:10px;font-size:9px;white-space:nowrap}
.post h4{margin-top:14px;font-size:9.5px;font-weight:700;color:#2d3e50;letter-spacing:.3px}
.post p{margin-top:7px;font-size:9px;line-height:14.5px;letter-spacing:.2px;white-space:nowrap}
.post .read-more{margin-top:12px}

/* footer */
.footer{left:0;top:978px;width:750px;height:195px;background:var(--navy)}
.footer h5{position:absolute;font-size:14px;font-weight:600;color:var(--white);letter-spacing:.5px}
.footer .info{position:absolute;font-size:9px;color:var(--footer-text);line-height:13.5px;letter-spacing:.2px}
.footer .links{position:absolute;list-style:none}
.footer .links li{font-size:8.5px;color:var(--footer-link);border-bottom:1px solid #3e5677;height:18px;line-height:16px;letter-spacing:.3px}
.notch{position:absolute;left:240px;top:0}
.foot-brand{position:absolute;left:242px;top:64px;width:94px;text-align:center;font-size:17px;font-weight:700;color:var(--white)}
.foot-social{position:absolute;left:254px;top:103px;display:flex;gap:5px}
.foot-social span{width:14px;height:14px;border-radius:50%;background:#8b98a8}
.bottom-bar{left:0;top:1173px;width:750px;height:27px;background:var(--navy-dark);text-align:center;font-size:8.5px;line-height:27px;color:#6d82a0;letter-spacing:.4px}
</style>
</head>
<body>

<header>
  <div class="abs brand"><span class="brand-dot"></span><span class="brand-name">MARAVEL</span></div>
  <div class="abs phone">
    <svg width="16" height="16" viewBox="0 0 24 24"><path d="M6.6 10.8a15 15 0 0 0 6.6 6.6l2.2-2.2a1 1 0 0 1 1-.25 11.4 11.4 0 0 0 3.6.6 1 1 0 0 1 1 1V20a1 1 0 0 1-1 1A17 17 0 0 1 3 4a1 1 0 0 1 1-1h3.5a1 1 0 0 1 1 1c0 1.25.2 2.45.6 3.6a1 1 0 0 1-.25 1z" fill="#55657a"/></svg>
    <span>(+613) 5550 2186</span>
  </div>
  <div class="abs social"><span></span><span></span><span></span><span></span></div>
</header>

<nav class="abs nav">
  <ul>
    <li class="active">Home</li><li>About Us</li><li>Our Services</li><li>Solutions</li><li>What's Happening</li><li>Contact Us</li>
  </ul>
  <span class="divider"></span>
  <span class="search">Search</span>
</nav>

<section class="abs hero">
  <div class="hero-photo" role="img" aria-label="Businesswoman drawing back a blue curtain to reveal an open road through mountains"></div>
  <svg class="hero-arrow" style="left:36px" width="30" height="56" viewBox="0 0 30 56"><path d="M27 2 3 28l24 26" fill="none" stroke="#fff" stroke-width="3"/></svg>
  <svg class="hero-arrow" style="left:684px" width="30" height="56" viewBox="0 0 30 56"><path d="M3 2l24 26L3 54" fill="none" stroke="#fff" stroke-width="3"/></svg>
  <h1 class="tagline">A New Way of Thinking</h1>
</section>

<section>
  <div class="abs feature" style="left:64px">
    <h3>TRANSFORMATION SPECIALISTS</h3>
    <svg style="margin:10px 0 0 35px;display:block" width="50" height="40" viewBox="0 0 50 40"><path d="M8 3h42v37H0V10z" fill="#eeeeee"/><rect x="15" y="13" width="20" height="14" fill="none" stroke="#555" stroke-width="1.4"/><rect x="18" y="16" width="14" height="8" fill="none" stroke="#555" stroke-width="1"/></svg>
    <p style="margin-top:13px">Nulla ut semper augue, eget euis-<br>mod quam. Quisque vel ligula nunc.<br>Suspendisse eleifend massa molestie</p>
    <div class="read-more" style="margin:17px 0 0 19px">Read More <svg width="20" height="6"><path d="M0 3h18M15 0l4 3-4 3" fill="none" stroke="#3d64a4"/></svg></div>
  </div>
  <div class="abs feature" style="left:287px">
    <h3 style="margin-left:15px">INNOVATIVE SOLUTIONS</h3>
    <svg style="margin:12px 0 0 60px;display:block" width="30" height="30" viewBox="0 0 30 30" fill="none" stroke="#555" stroke-width="1.2"><path d="M15 8a6 6 0 0 0-3.5 11v4h7v-4A6 6 0 0 0 15 8zM12 25h6M13 27h4M15 2v3M6 5l2 2M24 5l-2 2M3 13h3M24 13h3"/></svg>
    <p style="margin-top:14px">Nulla ut semper augue, eget euis-<br>mod quam. Quisque vel ligula nunc.<br>Suspendisse eleifend massa molestie</p>
    <div class="read-more" style="margin:24px 0 0 43px">Read More <svg width="20" height="6"><path d="M0 3h18M15 0l4 3-4 3" fill="none" stroke="#3d64a4"/></svg></div>
  </div>
  <div class="abs feature" style="left:513px">
    <h3 style="margin-left:9px">DIGITAL TRANSFORMATION</h3>
    <svg style="margin:11px 0 0 83px;display:block" width="26" height="30" viewBox="0 0 26 30"><circle cx="10" cy="9" r="7" fill="none" stroke="#777" stroke-width="1.3"/><path d="M8 9v13l-3-3-2 2 6 8h12l2-10-9-3V9z" fill="#555"/></svg>
    <p style="margin-top:14px">Nulla ut semper augue, eget euis-<br>mod quam. Quisque vel ligula nunc.<br>Suspendisse eleifend massa molestie</p>
    <div class="read-more" style="margin:25px 0 0 51px">Read More <svg width="20" height="6"><path d="M0 3h18M15 0l4 3-4 3" fill="none" stroke="#3d64a4"/></svg></div>
  </div>
</section>

<h2 class="abs section-title">LATEST POST FROM THE BLOG</h2>

<section>
  <article class="abs post" style="left:64px">
    <div class="post-photo" role="img" aria-label="Business team shaking hands around a meeting table" style="background:linear-gradient(135deg,#2a3644,#6f88a3 55%,#c9d8e6)"></div>
    <div class="meta">On: December 1, 2015 | Category: Blog</div>
    <h4>Nulla ut semper augue, eget.</h4>
    <p>Nulla ut semper augue, eget euismod<br>quam. Quisque vel ligula nunc. Sus-<br>pendisse eleifend massa molestie</p>
    <div class="read-more" style="margin-left:18px">Read More <svg width="20" height="6"><path d="M0 3h18M15 0l4 3-4 3" fill="none" stroke="#3d64a4"/></svg></div>
  </article>
  <article class="abs post" style="left:275px">
    <div class="post-photo" role="img" aria-label="Hand touching a glowing digital interface" style="background:radial-gradient(circle at 45% 55%,#a9c7e6,#3d5f93 55%,#1e2f55)"></div>
    <div class="meta">On: December 1, 2015 | Category: Blog</div>
    <h4>Nulla ut semper augue, eget.</h4>
    <p>Nulla ut semper augue, eget euismod<br>quam. Quisque vel ligula nunc. Sus-<br>pendisse eleifend massa molestie</p>
    <div class="read-more" style="margin-left:54px">Read More <svg width="20" height="6"><path d="M0 3h18M15 0l4 3-4 3" fill="none" stroke="#3d64a4"/></svg></div>
  </article>
  <article class="abs post" style="left:487px">
    <div class="post-photo" role="img" aria-label="Hands working on a tablet and documents at a desk" style="background:linear-gradient(160deg,#dce8f3,#9db6cf 55%,#6f8aa8)"></div>
    <div class="meta">On: December 1, 2015 | Category: Blog</div>
    <h4>Nulla ut semper augue, eget.</h4>
    <p>Nulla ut semper augue, eget euismod<br>quam. Quisque vel ligula nunc. Sus-<br>pendisse eleifend massa molestie</p>
    <div class="read-more" style="margin-left:76px">Read More <svg width="20" height="6"><path d="M0 3h18M15 0l4 3-4 3" fill="none" stroke="#3d64a4"/></svg></div>
  </article>
</section>

<footer class="abs footer">
  <svg class="notch" width="94" height="56" viewBox="0 0 94 56"><path d="M0 0h94L60 50a14 14 0 0 1-26 0z" fill="#fff"/><circle cx="47" cy="22" r="16" fill="var(--navy)"/></svg>
  <div class="foot-brand">MARAVEL</div>
  <div class="foot-social"><span></span><span></span><span></span><span></span></div>

  <h5 style="left:64px;top:19px">Contact Us</h5>
  <svg class="abs" style="left:57px;top:50px" width="14" height="18" viewBox="0 0 14 18"><path d="M7 1a6 6 0 0 0-6 6c0 4 6 10 6 10s6-6 6-10a6 6 0 0 0-6-6z" fill="none" stroke="#c9d3df" stroke-width="1.2"/><circle cx="7" cy="7" r="2" fill="none" stroke="#c9d3df"/></svg>
  <div class="info" style="left:84px;top:48px">PO Box 418<br>Harbour Lane East<br>Victoria 8010<br>AUSTRALIA</div>
  <svg class="abs" style="left:56px;top:128px" width="16" height="16" viewBox="0 0 24 24"><path d="M6.6 10.8a15 15 0 0 0 6.6 6.6l2.2-2.2a1 1 0 0 1 1-.25 11.4 11.4 0 0 0 3.6.6 1 1 0 0 1 1 1V20a1 1 0 0 1-1 1A17 17 0 0 1 3 4a1 1 0 0 1 1-1h3.5a1 1 0 0 1 1 1c0 1.25.2 2.45.6 3.6a1 1 0 0 1-.25 1z" fill="#e4eaf1"/></svg>
  <div class="info" style="left:82px;top:128px;line-height:18.5px">1300 555 218 (Aus)<br>0800 555 218 (NZ)<br>1300 555 219 (Intl)</div>

  <h5 style="left:409px;top:22px">About Us</h5>
  <ul class="links" style="left:409px;top:55px;width:73px">
    <li>Our Team</li><li>Our Values</li><li>Giving Back</li>
  </ul>

  <h5 style="left:553px;top:22px">Our Services</h5>
  <ul class="links" style="left:552px;top:54px;width:140px">
    <li>Strategy and Design</li><li>Transformation</li><li>Change &amp; Culture</li><li>Organisational Development</li><li>Project Management</li><li>Organisational Efficiency</li><li>Specialist Placements</li>
  </ul>
</footer>

<div class="abs bottom-bar">Copyright © 2016 Maravel Global Solutions</div>

</body>
</html>
```